Event Website Design

We need a new website design for an events driven website. The domain for this site is http://brackenmoorhalls.co.uk. The site is up and running but needs a new fresh, modern look.
I've attached a Balamiq Mockup for the layout of the home page. Also attached is a png of the logo.
Key colours for the site are 0f7e6a, 35bde, d57835 & 373737.
Font to use is Proxima Nova
Width of the site should be 1200px
The design should be contemporary with minimal clutter.
Websites to references are…
http://vantorium.london/
http://www.thegpz.co.uk/
These are just guidelines, please feel free to use you own creative judgment.
The selected design file needs to be supplied as an editable PSD.
Reason: I've submitted 5 designs to the client, who will select the one they want. I will then choose that design. So please be patient as I'm waiting for a decision from my client.
Events
1 page

```html
<!DOCTYPE html>
<html lang="en">
<head>
<meta charset="utf-8">
<title>Brackenmoor Halls – Home</title>
<link href="https://fonts.googleapis.com/css2?family=Figtree:wght@400;500;600;700&display=swap" rel="stylesheet">
<style>
:root{
  --charcoal:#373737;
  --charcoal-dark:#2d2d2d;
  --teal:#0f7e6a;
  --orange:#d57835;
  --blue:#1f5fde;
  --paper:#efefef;
  --white:#ffffff;
  --ink:#333333;
  --muted:#777777;
}
*{box-sizing:border-box;margin:0;padding:0}
html,body{width:1200px;height:2715px;overflow:hidden}
body{font-family:"Figtree",Arial,sans-serif;color:var(--ink);background:var(--white);position:relative}
a{color:inherit;text-decoration:none}

/* header */
.site-header{position:absolute;left:0;top:0;width:1200px;height:172px;background:var(--charcoal);color:var(--white)}
.utility-links{position:absolute;right:73px;top:13px;font-size:10.5px;letter-spacing:.3px;color:#d8d8d8}
.utility-links span{margin:0 4px}
.box-office{position:absolute;left:72px;top:84px;font-size:19px;color:#eee}
.box-office strong{color:var(--orange);font-weight:500}
.brand{position:absolute;left:0;width:1200px;top:80px;text-align:center}
.brand-name{display:inline-flex;align-items:center;gap:10px;font-size:25px;font-weight:700;letter-spacing:1px;color:var(--white)}
.brand-name i{display:inline-block;width:16px;height:16px;background:var(--teal)}
.tagline{position:absolute;left:0;width:1200px;top:134px;text-align:center;font-size:13.5px;color:#eee}
.search{position:absolute;left:917px;top:81px;width:210px;height:32px;border-radius:16px;background:var(--white);font-size:11px;color:#aaa;padding:9px 0 0 34px}
.search svg{position:absolute;left:12px;top:9px}

.main-nav{position:absolute;left:0;top:172px;width:1200px;height:47px;background:var(--charcoal-dark);display:flex;justify-content:center;gap:40px;align-items:center;font-size:11.5px;color:#f0f0f0;letter-spacing:.3px}

/* hero */
.hero{position:absolute;left:0;top:219px;width:1200px;height:553px;background:linear-gradient(120deg,#6f6a66,#a69a92 45%,#5c5b62)}
.hero-panel{position:absolute;left:795px;top:219px;width:330px;height:418px;background:rgba(15,126,106,.93);color:var(--white);padding:28px 28px}
.date-tag{display:inline-block;background:var(--orange);color:var(--white);font-size:12px;padding:4px 8px}
.hero-panel h1{font-size:23px;font-weight:500;line-height:1.15;margin-top:14px}
.hero-panel p{font-size:12.5px;line-height:1.6;margin-top:22px}
.btn{display:inline-block;border:2px solid currentColor;text-align:center;font-size:12px;letter-spacing:.5px}
.hero-actions{position:absolute;left:44px;top:297px;display:flex;gap:10px}
.hero-actions .btn{width:115px;height:40px;line-height:36px}
.hero-progress{position:absolute;left:222px;top:772px;width:298px;height:8px;background:var(--orange)}

/* event tiles */
.event-strip{position:absolute;left:0;top:783px;width:1200px;height:302px;display:flex;gap:2px}
.event-tile{position:relative;flex:1;color:var(--white)}
.event-tile .photo{position:absolute;inset:0}
.event-tile .info{position:absolute;left:25px;top:155px}
.event-tile .date-tag{background:var(--teal);font-size:11px;padding:3px 6px}
.event-tile h3{font-size:16px;font-weight:500;line-height:1.3;margin-top:12px}
.tile-actions{display:flex;gap:10px;margin-top:12px}
.tile-actions .btn{width:89px;height:30px;line-height:26px;font-size:12px}
.tile-actions .book{color:var(--orange)}
.tile-actions .more{color:var(--white)}

/* news */
.news{position:absolute;left:0;top:1085px;width:1200px;height:463px;background:var(--paper)}
.section-title{position:absolute;left:0;width:1200px;top:50px;text-align:center;font-size:23px;font-weight:500;color:var(--ink)}
.section-sub{position:absolute;left:0;width:1200px;top:82px;text-align:center;font-size:12px;color:var(--muted)}
.news-card{position:absolute;top:137px;width:333px;height:270px;background:var(--white)}
.news-card header{height:92px;background:var(--orange);color:var(--white);padding:24px 28px;font-size:17px;font-weight:500;line-height:1.3}
.news-card p{font-size:12.5px;line-height:1.8;color:#666;padding:22px 28px 0}
.news-card .more-link{position:absolute;right:0;bottom:0;width:333px;height:17px;background:#fbeee4;text-align:right;padding-right:10px;font-size:11px;line-height:17px;color:var(--orange)}

/* feature cards */
.feature{position:absolute;top:1602px;width:333px;height:356px}
.feature .photo{position:absolute;left:0;top:0;width:333px;height:240px}
.feature .panel{position:absolute;left:0;top:240px;width:333px;height:116px;color:var(--white);text-align:center}
.feature h3{font-size:17px;font-weight:500;margin-top:22px;letter-spacing:.3px}
.feature .btn{width:88px;height:30px;line-height:26px;margin-top:14px;font-size:12px}
.feature .badge{position:absolute;left:136px;top:-38px}
.conferences .panel{background:var(--blue)}
.parties .panel{background:var(--teal)}
.coworking .panel{background:var(--orange)}

/* sports */
.sports{position:absolute;left:0;top:2015px;width:1200px;height:462px;background:linear-gradient(90deg,#b9846b,#c9a99a 35%,#6a8fb5 65%,#5c5550)}
.sports h2{position:absolute;left:0;width:1200px;top:190px;text-align:center;font-size:44px;font-weight:500;color:var(--white);letter-spacing:1px}
.sports p{position:absolute;left:0;width:1200px;top:243px;text-align:center;font-size:12px;color:var(--white);letter-spacing:.5px}

/* footer */
.site-footer{position:absolute;left:0;top:2477px;width:1200px;height:238px;background:var(--charcoal);color:#d0d0d0;font-size:12.5px;line-height:1.8}
.footer-col{position:absolute;top:39px}
.footer-brand{position:absolute;left:905px;top:88px}
.footer-brand .brand-name{font-size:26px}
.copyright{position:absolute;left:0;width:1200px;top:192px;text-align:center;font-size:12px;color:#bbb}
</style>
</head>
<body>

<header class="site-header">
  <nav class="utility-links"><a>GIFT VOUCHER</a><span>|</span><a>JOIN OUR MAILING LIST</a><span>|</span><a>MY ACCOUNT</a><span>|</span><a>BASKET</a><span>|</span><a>REGISTER</a></nav>
  <div class="box-office">Box Office : <strong>01632 960 482</strong></div>
  <div class="brand"><span class="brand-name"><i></i>BRACKENMOOR HALLS</span></div>
  <div class="tagline">Somerset's Premier Entertainment &amp; Sporting Center</div>
  <div class="search">
    <svg width="13" height="13" viewBox="0 0 13 13"><circle cx="5.5" cy="5.5" r="4.2" fill="none" stroke="#888" stroke-width="1.5"/><line x1="8.5" y1="8.5" x2="12" y2="12" stroke="#888" stroke-width="1.5"/></svg>
    Search
  </div>
</header>

<nav class="main-nav">
  <a>WHAT'S ON</a><a>CONFERENCING &amp; EVENTS</a><a>SPORTS &amp; LEISURE</a><a>LANTERN THEATRE</a><a>PLAN YOUR VISIT</a><a>NEWS</a><a>DISCOVER MORE</a><a>CONTACT</a>
</nav>

<section class="hero" role="img" aria-label="Guests mingling and talking at a drinks reception"></section>
<div class="hero-panel">
  <span class="date-tag">MONDAY 7 JAN 2017</span>
  <h1>THE STANDARD<br>LOREM IPSUM PASSAGE</h1>
  <p>Lorem ipsum dolor sit amet, consectetur adipiscing elit, sed do eiusmod tempor incididunt ut labore et dolore magna aliqua. Ut enim ad minim veniam, quis nostrud exercitation ullamco laboris nisi ut aliquip ex ea commodo consequat.</p>
  <div class="hero-actions"><a class="btn">MORE</a><a class="btn">BOOK</a></div>
</div>
<div class="hero-progress"></div>

<section class="event-strip">
  <article class="event-tile">
    <div class="photo" role="img" aria-label="Large concert crowd under stage lights" style="background:linear-gradient(180deg,#6f6a9a,#3b3450)"></div>
    <div class="info"><span class="date-tag">MONDAY 7 JAN 2017</span><h3>The standard<br>Lorem Ipsum passage</h3><div class="tile-actions"><a class="btn more">MORE</a><a class="btn book">BOOK</a></div></div>
  </article>
  <article class="event-tile">
    <div class="photo" role="img" aria-label="Busy trade exhibition hall with stands" style="background:linear-gradient(180deg,#8a9aa8,#3c3a3a)"></div>
    <div class="info"><span class="date-tag">MONDAY 7 JAN 2017</span><h3>The standard<br>Lorem Ipsum passage</h3><div class="tile-actions"><a class="btn more">MORE</a><a class="btn book">BOOK</a></div></div>
  </article>
  <article class="event-tile">
    <div class="photo" role="img" aria-label="Evening venue interior with warm ceiling lights" style="background:linear-gradient(180deg,#6b5a2c,#2a2a22)"></div>
    <div class="info"><span class="date-tag">MONDAY 7 JAN 2017</span><h3>The standard<br>Lorem Ipsum passage</h3><div class="tile-actions"><a class="btn more">MORE</a><a class="btn book">BOOK</a></div></div>
  </article>
  <article class="event-tile">
    <div class="photo" role="img" aria-label="Outdoor festival crowd with marquees" style="background:linear-gradient(180deg,#9fb7a5,#4f5e3e)"></div>
    <div class="info"><span class="date-tag">MONDAY 7 JAN 2017</span><h3>The standard<br>Lorem Ipsum passage</h3><div class="tile-actions"><a class="btn more">MORE</a><a class="btn book">BOOK</a></div></div>
  </article>
</section>

<section class="news">
  <h2 class="section-title">LATEST FROM BRACKENMOOR</h2>
  <div class="section-sub">See All News</div>
  <article class="news-card" style="left:73px">
    <header>The standard Lorem Ipsum<br>passage used since.</header>
    <p>Ut enim ad minim veniam, quis nostrud Duis aute irure dolor in reprehenderit in cillum dolore eu fugiat nulla pariatur. Ut aute irure dolor in reprehenderit in cillum dolore eu fugiat nulla pariatur.</p>
    <a class="more-link">MORE ▸</a>
  </article>
  <article class="news-card" style="left:434px">
    <header>The standard Lorem Ipsum<br>passage used since.</header>
    <p>Ut enim ad minim veniam, quis nostrud Duis aute irure dolor in reprehenderit in cillum dolore eu fugiat nulla pariatur. Ut aute irure dolor in reprehenderit in cillum dolore eu fugiat nulla pariatur.</p>
    <a class="more-link">MORE ▸</a>
  </article>
  <article class="news-card" style="left:794px">
    <header>The standard Lorem Ipsum<br>passage used since.</header>
    <p>Ut enim ad minim veniam, quis nostrud Duis aute irure dolor in reprehenderit in cillum dolore eu fugiat nulla pariatur. Ut aute irure dolor in reprehenderit in cillum dolore eu fugiat nulla pariatur.</p>
    <a class="more-link">MORE ▸</a>
  </article>
</section>

<article class="feature conferences" style="left:73px">
  <div class="photo" role="img" aria-label="Speaker addressing a seated conference audience" style="background:linear-gradient(180deg,#8a4a2c,#3a2a2a)"></div>
  <div class="panel">
    <svg class="badge" width="62" height="62" viewBox="0 0 62 62"><polygon points="31,2 57,17 57,45 31,60 5,45 5,17" fill="var(--blue)"/></svg>
    <h3>CONFERENCES &amp; EVENTS</h3><a class="btn">MORE</a>
  </div>
</article>
<article class="feature parties" style="left:434px">
  <div class="photo" role="img" aria-label="Friends laughing together at an evening party" style="background:linear-gradient(180deg,#5a4a44,#2e2a2a)"></div>
  <div class="panel">
    <svg class="badge" width="62" height="62" viewBox="0 0 62 62"><polygon points="31,2 57,17 57,45 31,60 5,45 5,17" fill="var(--teal)"/></svg>
    <h3>PARTIES AT BRACKENMOOR</h3><a class="btn">MORE</a>
  </div>
</article>
<article class="feature coworking" style="left:794px">
  <div class="photo" role="img" aria-label="Hands typing on a laptop keyboard" style="background:linear-gradient(180deg,#b0a8a2,#4c4a4a)"></div>
  <div class="panel">
    <svg class="badge" width="62" height="62" viewBox="0 0 62 62"><polygon points="31,2 57,17 57,45 31,60 5,45 5,17" fill="var(--orange)"/></svg>
    <h3>CO-WORKING HUB</h3><a class="btn">MORE</a>
  </div>
</article>

<section class="sports" role="img" aria-label="People running on treadmills in a gym">
  <h2>SPORTS &amp; LEISURE</h2>
  <p>CLICK FOR MORE INFORMATION</p>
</section>

<footer class="site-footer">
  <div class="footer-col" style="left:73px">Brackenmoor Entertainment Venue<br>Bracken Lane<br>Harrowfield<br>Somerset<br>HF4 2QT</div>
  <div class="footer-col" style="left:345px">What's On<br>Conferencing &amp; Events<br>Sports &amp; Leisure<br>Lantern Theatre</div>
  <div class="footer-col" style="left:614px">Plan Your Visit<br>News<br>Discover More<br>Contact Us</div>
  <div class="footer-brand"><span class="brand-name"><i></i>BRACKENMOOR</span></div>
  <div class="copyright">Copyright © 2016 brackenmoorhalls.co.uk All Rights Reserved</div>
</footer>

</body>
</html>
```